Presentation Folder Saguaro Plan Advisors

I would like a two sided presentation folder 9" wide x 12" tall for our benefits/ insurance company. It must be professional and instill confidence in our customers. ArtHive designed our logo which must be included. Our website is www.spallc-example.org The logo on the website is the old one as a new website is about to launch. The contact information and address are correct on the website. We provide health, disability and other benefits to employers and will use this when making presentations about plans and renewals. I have been told to put this as stationery from someone at ArtHive but it is not stationery. Please feel free to email me if you have questions.

Reason: My committee meets Oct. 17.

```html
<!DOCTYPE html>
<html lang="en">
<head>
<meta charset="utf-8">
<title>Saguaro Plan Advisors — Presentation Folder</title>
<link rel="stylesheet" href="https://fonts.googleapis.com/css2?family=Cinzel:wght@700&family=Tinos&display=swap">
<style>
  :root {
    --navy: #100b3f;
    --brand-navy: #2e2a6e;
    --gold: #d59f42;
    --fold: #c9a060;
    --paper: #ffffff;
  }
  html, body {
    margin: 0;
    padding: 0;
    overflow: hidden;
    background: var(--paper);
  }
  .folder {
    position: relative;
    width: 1200px;
    height: 924px;
    overflow: hidden;
    background: var(--paper);
  }
  .folder-art {
    position: absolute;
    inset: 0;
  }
  .brand-name {
    margin: 0;
    font-family: "Cinzel", serif;
    font-weight: 700;
    line-height: 1.08;
    letter-spacing: 0.01em;
  }
  .brand-name--cover {
    position: absolute;
    left: 52px;
    top: 160px;
    font-size: 40px;
    color: var(--brand-navy);
  }
  .back-panel {
    position: absolute;
    left: 701px;
    top: 640px;
    width: 420px;
    text-align: center;
    color: var(--paper);
  }
  .brand-name--back {
    font-size: 17px;
    color: var(--paper);
    margin-bottom: 20px;
  }
  .contact {
    font-family: "Tinos", serif;
    margin: 0;
    line-height: 1.4;
  }
  .contact-phone { font-size: 18px; margin-bottom: 1px; }
  .contact-line { font-size: 15.5px; }
</style>
</head>
<body>
<div class="folder">
  <svg class="folder-art" width="1200" height="924" viewBox="0 0 1200 924" aria-hidden="true">
    <path class="wave-gold" fill="var(--gold)"
      d="M0 511 C150 600 300 664 400 664 C500 664 560 640 600 600 C680 540 720 420 780 370 C860 290 980 262 1080 262 C1140 262 1180 265 1200 268 L1200 924 L0 924 Z"/>
    <path class="wave-navy" fill="var(--navy)"
      d="M0 532 C150 615 300 680 400 680 C500 680 565 650 605 610 C685 550 725 425 785 380 C865 310 980 278 1080 278 C1140 278 1180 283 1200 287 L1200 924 L0 924 Z"/>
    <g class="fold-lines" stroke="var(--fold)" stroke-width="1" fill="none">
      <rect x="0.5" y="0.5" width="1199" height="923"/>
      <line x1="600" y1="0" x2="600" y2="798"/>
      <line x1="0" y1="798" x2="1200" y2="798"/>
    </g>
  </svg>

  <h1 class="brand-name brand-name--cover">Saguaro Plan<br>Advisors</h1>

  <div class="back-panel">
    <p class="brand-name brand-name--back">Saguaro Plan Advisors</p>
    <p class="contact contact-phone">555-010-4821</p>
    <p class="contact contact-line">info@spallc-example.com</p>
    <p class="contact contact-line">456 Canyon Avenue, Mesa Ridge, Arizona 85099</p>
  </div>
</div>
</body>
</html>
```